International PR and marketing agency needs website design

We need a branding website, for a company based in the US (Washington DC). We are a communication (PR, marketing, social media) agency. We already have the copy, and we have some example websites (some major agencies), that we like.
For example:
https://tallorquinbeam.example/
https://zurvexglobal.example/
https://pemrat.example/
https://qfn-omnis.example/
https://www.roskavert.example/
The website must be a multi-language site, we will add the new languages step-by-step.
We would like to upload content continuously.
The website has to have sub-pages (segments), and news part.
Target Market(s)
Global
Industry/Entity Type
Public relations, Communications, Marketing, Social Media
Number of Pages Required
5+ page
Font styles to use
Other font styles liked:
- Well readable, modern style.
Look and feel
Each slider illustrates characteristics of the customer's brand and the style your logo design should communicate.

```html
<!DOCTYPE html>
<html lang="en">
<head>
<meta charset="utf-8">
<title>Kavelin PR — Communication Agency</title>
<link href="https://fonts.googleapis.com/css2?family=Poppins:wght@400;500;600;700&display=swap" rel="stylesheet">
<style>
:root{
  --red:#e30613;
  --crimson:#c8102e;
  --plum:#96105f;
  --blush:#e4c0d5;
  --ink:#222;
  --cream:#fbf7f6;
  --black:#050505;
  --grad:linear-gradient(180deg,var(--red) 0%,var(--plum) 100%);
}
*{margin:0;padding:0;box-sizing:border-box}
html,body{width:1200px;height:4109px;overflow:hidden}
body{font-family:"Poppins",sans-serif;color:var(--ink);background:#fff;position:relative}
.abs{position:absolute}
.btn{position:absolute;display:flex;align-items:center;justify-content:center;background:var(--grad);color:#fff;font-size:13px;font-weight:500;text-decoration:none}
.btn.light{background:#fff;color:var(--crimson)}
.title{color:var(--crimson);font-weight:700;font-size:31px}

/* header */
.site-header{position:absolute;left:0;top:0;width:1200px;height:116px;background:var(--cream)}
.brand{position:absolute;left:112px;top:30px;font-size:34px;font-weight:700;color:var(--red);letter-spacing:-1px}
.nav{position:absolute;left:389px;top:52px;display:flex;gap:33px;font-size:12.5px}
.nav a{color:var(--ink);text-decoration:none}
.lang{position:absolute;left:945px;top:37px;width:75px;height:41px;background:var(--plum);display:flex;align-items:center;justify-content:center}
.search{position:absolute;left:1058px;top:45px}

/* hero */
.hero{position:absolute;left:0;top:116px;width:1200px;height:588px;background:radial-gradient(circle at 76% 33%,#8a6a4a 0%,#3a4658 22%,#2b2f38 48%,#262626 100%)}
.hero h1{position:absolute;left:112px;top:110px;color:#fff;font-size:45px;font-weight:700}
.hero p{position:absolute;left:112px;top:203px;width:480px;color:#fff;font-size:17.5px;font-weight:600;line-height:31px}
.hero .btn{left:112px;top:398px;width:122px;height:42px}
.dots{position:absolute;left:574px;top:511px;display:flex;gap:5px}
.dots span{width:8px;height:8px;border-radius:50%;background:#fff}
.dots span:first-child{background:var(--red);width:10px;height:10px;margin-top:-1px}

/* round photos */
.ring{position:absolute;width:428px;height:428px;border-radius:50%;background:var(--grad)}
.ring .photo{position:absolute;left:20px;top:20px;width:388px;height:388px;border-radius:50%;border:4px solid #fff}

.copy h2{font-size:31px;font-weight:700;color:var(--crimson)}
.copy h3{font-size:21px;font-weight:400;margin-top:14px}
.copy p{font-size:12.5px;line-height:21px}

/* expertise */
.band{position:absolute;left:0;top:1499px;width:1200px;height:747px;background:var(--blush)}
.tile{position:absolute;top:1380px;width:210px;height:210px;border-radius:50%;background:var(--grad);color:#fff;font-size:20px;font-weight:600;text-align:center}
.tile.active{background:#fff;color:var(--crimson);box-shadow:0 0 0 3px #f3e3ec}
.tile svg{position:absolute;left:65px;top:36px}
.tile span{position:absolute;left:0;right:0;top:136px}
.card{position:absolute;top:1644px;width:301px}
.card .img{width:301px;height:300px}
.card h4{position:absolute;top:314px;left:0;color:var(--crimson);font-size:21px;font-weight:600;line-height:30px}
.card p{position:absolute;top:362px;left:0;font-size:12px;line-height:21px;width:318px;letter-spacing:-0.1px}
.card .arrow{position:absolute;top:500px;left:0}

/* philosophy */
.philosophy{position:absolute;left:0;top:2630px;width:1200px;height:453px;background:var(--grad)}
.philosophy h2{position:absolute;left:111px;top:60px;color:#fff;font-size:33px;font-weight:700}
.philosophy p{position:absolute;left:112px;width:500px;color:#fff;font-size:12.5px;line-height:21px}

/* footer */
.footer{position:absolute;left:0;top:3685px;width:1200px;height:424px;background:var(--black);color:#fff;text-align:center}
.footer h5{font-size:21px;font-weight:600}
.footer p{font-size:12.5px;line-height:21px}
.footer .rule{position:absolute;left:0;top:364px;width:1200px;height:1px;background:#3a3a3a}
</style>
</head>
<body>

<header class="site-header">
  <div class="brand">kavelin</div>
  <nav class="nav">
    <a href="#">Who We Are</a><a href="#">Our Expertise</a><a href="#">News</a><a href="#">Our Work</a><a href="#">KavLink</a><a href="#">Contact</a>
  </nav>
  <div class="lang"><svg width="30" height="28" viewBox="0 0 30 28" fill="none" stroke="#fff" stroke-width="1.6"><rect x="2" y="2" width="15" height="16"/><rect x="13" y="9" width="15" height="16"/><path d="M6 13l3.5-8 3.5 8M7.3 10.5h4.5M17 14h8M21 12v2M24 14c-1 4-4 6-6 7M19 17c1 2 3 3 5 4"/></svg></div>
  <svg class="search" width="30" height="30" viewBox="0 0 30 30" fill="none" stroke="var(--plum)" stroke-width="3"><circle cx="12" cy="12" r="9"/><path d="M19 19l9 9"/></svg>
</header>

<section class="hero">
  <div class="abs" style="left:0;top:0;width:1200px;height:588px" role="img" aria-label="Hand holding a glowing globe surrounded by connected digital icons"></div>
  <h1>Welcome to Kavelin PR</h1>
  <p>Lorem ipsum dolor sit amet, consectetur adipiscing elit, sed do eiusmod tempor incididunt ut labore et dolore magna aliqua. Ut enim ad minim veniam, quis nostrud exercitation ullamco laboris nisi ut aliquip ex ea commodo consequat.</p>
  <a class="btn" href="#">Read More</a>
  <div class="dots"><span></span><span></span><span></span><span></span></div>
</section>

<!-- about -->
<div class="ring" style="left:112px;top:788px"><div class="photo" role="img" aria-label="Two colleagues working together at a laptop in an office" style="background:linear-gradient(135deg,#d9dde2,#b7bec6 55%,#8a8f96)"></div></div>
<div class="copy abs" style="left:634px;top:858px;width:420px">
  <h2>About Us</h2>
  <h3>We are building relationships</h3>
  <p style="margin-top:30px">Thinking beyond media relations and marketing services, we understand the needs of our clients, and our experts and our creative staff are working on building long-term relationships. Anywhere in the world.</p>
</div>
<a class="btn" href="#" style="left:634px;top:1098px;width:122px;height:42px">Read More</a>

<!-- expertise -->
<div class="title abs" style="left:0;width:1200px;text-align:center;top:1298px">Our Expertise</div>
<div class="band"></div>

<div class="tile" style="left:112px">
  <svg width="80" height="80" viewBox="0 0 80 80" fill="none" stroke="#fff" stroke-width="5"><circle cx="40" cy="40" r="20"/><path d="M40 12v8M40 60v8M12 40h8M60 40h8M20 20l6 6M54 54l6 6M60 20l-6 6M26 54l-6 6"/><path d="M31 40l6 6 11-12" stroke-width="4"/></svg>
  <span>Practices</span>
</div>
<div class="tile" style="left:367px">
  <svg width="80" height="80" viewBox="0 0 80 80" fill="none" stroke="#fff" stroke-width="4"><path d="M18 36a18 18 0 0 1 36 0"/><rect x="13" y="34" width="8" height="14" rx="3"/><rect x="51" y="34" width="8" height="14" rx="3"/><path d="M14 72c2-12 10-18 22-18"/><rect x="42" y="50" width="30" height="20"/><path d="M57 70v6M50 76h14"/></svg>
  <span>ESport</span>
</div>
<div class="tile active" style="left:621px">
  <svg width="80" height="80" viewBox="0 0 80 80" fill="none" stroke="var(--crimson)" stroke-width="3.5"><rect x="24" y="6" width="30" height="68" rx="5"/><path d="M35 12h8"/><rect x="8" y="14" width="18" height="13" rx="3"/><path d="M15 18l4 2.5-4 2.5z"/><rect x="52" y="42" width="20" height="14" rx="3"/><path d="M56 47h12M56 51h8"/><path d="M30 66c2-8 6-11 10-11s8 3 10 11"/></svg>
  <span>Influencers</span>
  <svg style="left:96px;top:178px" width="18" height="18" viewBox="0 0 18 18"><path d="M5 4l9 6-4 1 3 5-2 1-3-5-3 3z" fill="#111"/></svg>
</div>
<div class="tile" style="left:875px">
  <svg width="80" height="80" viewBox="0 0 80 80" fill="none" stroke="#fff" stroke-width="4"><path d="M30 52c0-8-8-12-8-22a18 18 0 0 1 36 0c0 10-8 14-8 22z"/><path d="M32 60h16M34 67h12"/><path d="M40 2v6M12 12l5 5M68 12l-5 5M4 34h6M70 34h6"/></svg>
  <span>Other Solutions</span>
</div>

<article class="card" style="left:112px">
  <div class="img" role="img" aria-label="Printed bar charts with a magnifying glass on a wooden desk" style="background:linear-gradient(135deg,#a9c9e6,#e9e4d6 50%,#c9a57a)"></div>
  <h4>Trends</h4>
  <p>Companies – thanks to the internet and social – recognized that they can forward the information thought important by them much more easily and more cost-effectively people who are popular in certain target groups, so they turned to storytellers.</p>
  <svg class="arrow" width="52" height="32" viewBox="0 0 52 32" fill="none" stroke="var(--crimson)" stroke-width="4"><path d="M2 16h44M32 3l14 13-14 13"/></svg>
</article>
<article class="card" style="left:448px">
  <div class="img" role="img" aria-label="Blue technology graphic with the words Our Vision at its centre" style="background:radial-gradient(circle,#2a7bd6,#0d3c8a 60%,#061f55)"></div>
  <h4>Our Vision</h4>
  <p>We worked out our program for influencers and clients relying on the expectations towards complex services. As we represent many brands with the natural expectation to work together with the popular opinion leaders of the social media, we make a connection between the two parties.</p>
  <svg class="arrow" width="52" height="32" viewBox="0 0 52 32" fill="none" stroke="var(--crimson)" stroke-width="4"><path d="M2 16h44M32 3l14 13-14 13"/></svg>
</article>
<article class="card" style="left:784px">
  <div class="img" role="img" aria-label="Person with a tablet in a glowing blue server hall" style="background:linear-gradient(180deg,#0e2a4d,#1f5f9a 55%,#0b1e36)"></div>
  <h4>Future</h4>
  <p>We have never seen as much content created by influencers as now. More and more photo and video materials are available for them, many "artists" with a huge follower base emerged in the last few years.</p>
  <svg class="arrow" width="52" height="32" viewBox="0 0 52 32" fill="none" stroke="var(--crimson)" stroke-width="4"><path d="M2 16h44M32 3l14 13-14 13"/></svg>
</article>

<!-- our work -->
<div class="title abs" style="left:0;width:1200px;text-align:center;top:2334px">Our Work</div>
<div class="abs" style="left:0;width:1200px;text-align:center;top:2390px;font-size:21px">We are creating unique values</div>
<div class="abs" style="left:0;width:1200px;text-align:center;top:2438px;font-size:12.5px;line-height:22px">Our experts, creative staff and data analysts are up to the most extraordinary challenges on all parts of the world.<br>This is not only the beginning of a business relationship, for us, it means much more.</div>
<a class="btn" href="#" style="left:539px;top:2504px;width:122px;height:42px">Learn More</a>

<!-- philosophy -->
<section class="philosophy">
  <h2>Philosophy</h2>
  <p style="top:134px">Our work goes way beyond media relations and marketing services. Our creators and colleagues prepare such campaigns and designs that not only provide the competitive advantage and attention our clients need, but also create values and interaction that last for more generations.</p>
  <p style="top:234px">For us, it is extremely important to support transparent business processes, client-focused and ethical behavior though the principles and values laid down in our philosophy – that allows us to create true values.</p>
  <a class="btn light" href="#" style="left:112px;top:346px;width:122px;height:42px">Learn More</a>
  <svg class="abs" style="left:670px;top:0" width="530" height="453" viewBox="0 0 530 453">
    <path d="M108 0H530V446H112C55 380 40 310 44 226C48 130 70 60 108 0Z" fill="#fff"/>
    <path d="M114 0H530V440H118C64 378 50 310 54 226C58 132 78 62 114 0Z" fill="#8fa3b5" role="img" aria-label="Two colleagues smiling at a computer screen in a bright office"/>
  </svg>
</section>

<!-- global -->
<div class="ring" style="left:112px;top:3171px"><div class="photo" role="img" aria-label="Hands holding a smartphone projecting a network map with location pins" style="background:radial-gradient(circle at 45% 60%,#d98a3a,#3a5d7a 35%,#1c2b3c)"></div></div>
<div class="copy abs" style="left:634px;top:3211px;width:415px">
  <h2>Global Solution</h2>
  <p style="margin-top:24px">Our reach is endless. No matter where the challenge arises, we are there to help. We provide our services in several countries of the world, leaning on the support of our colleagues who are well-aware of the local conditions. This means we can reach any</p>
  <p style="margin-top:22px">And anywhere. We break down barriers, so by providing the perfect services, we can ensure the largest possible market advantage for our clients. We fight the challenges together on every field, which allows us to evolve in the meantime.</p>
</div>
<a class="btn" href="#" style="left:634px;top:3509px;width:122px;height:42px">Read More</a>

<footer class="footer">
  <h5 style="margin-top:58px">About Us</h5>
  <p style="margin:10px auto 0;width:560px">Thinking beyond media relations and marketing services, we understand the needs of our clients, and our experts and our creative staff are working on building long-term relationships. Anywhere in the world.</p>
  <h5 style="margin-top:20px">Contact Us</h5>
  <p style="margin-top:12px">Kavelin PR US (Washington DC), Suite 4120.<br>+1 555-014-2290<br>hello@kavelinpr.example</p>
  <div class="rule"></div>
  <p class="abs" style="left:0;width:1200px;top:386px;font-size:11.5px">Copyright © 2023 Kavelin PR. All rights reserved.</p>
</footer>

</body>
</html>
```